Revamp our software development company Wix site

We need to rework our Wix website theming, layout, design to match our logo file color and theming. There are a few elements we want to keep, such as the top splash 'typing' header.

The current site is hiketoucan.net. This website I created with Wix, but I never fully finished the copy and all sections.

The feel and mood of the site should be "Warm, professional, inviting, and should project expertise in the field, confidence." But not corporate and cold.

The colors and fonts should match the logo theming. The website must match the logo which was designed in a separate contest. So browns, greens, whites, etc. to create a warm and professional, but fun website.

I want to showcase our app development screenshots in a nice, sharp way.

We are a new company, with only a few clients and projects under our belt. So we don't have lots of need for many testimonials, project showcases, etc. just a couple which is why we went with "Recent work" instead of "Portfolio".

It needs a blog section also that looks great, and will allow me to manage the blog after this project is over. The blog's purpose is for SEO content and marketing.

It will be a huge win for the makerbazaar artist, to make something unique that doesn't look like every other templated website.

We can use the text/sections found on hiketoucan.net, then i would like to tweak some of the copy and sections later.

***This is a Wix website*** I think it would be 2 pages. The landing page, then the blog page.

***Awesome inspiration websites/vibes we like***
https://ninekitesworks.com/
https://vostrella.com/
https://www.larkspinmedia.com/
https://www.triplumeworks.com/
https://harbor-makerhaus.com/
https://frostquill.works/

If you have ideas that need to break free from Wix environment, I am open to that idea also. Wix is just easy for a non-technical founder like me to manage our site/blog.

Thanks!

Target Market(s)

Industry leading commercial and residential construction companies seeking custom software development

Industry/Entity Type

We are a boutique software development studio.

Coding

Coded - Design and coding required

Font styles to use
Sans Serif

Requirements
Must have
• Darker/warm background and overall feel. Relaxed and confident vibes. Simplicity, less is more approach. Blog page. Must have project gallery to showcase high res- screenshots. Clear sans serif fonts, nice contrasting colors.
Nice to have
• If it could have some sort of construction related flare, like photos or icon, that could be good, but it cannot be cheesy. A lot of the stock photos of construction workers etc. are terrible and cheesy (please do not use).
Should not have
• lots of pages, music/sounds, busy theming, tiny fonts

```html
<!DOCTYPE html>
<html lang="en">
<head>
<meta charset="utf-8">
<title>Toucan Studio — Custom software for construction</title>
<link rel="stylesheet" href="https://fonts.googleapis.com/css2?family=Arimo:wght@400;500;600;700&display=swap">
<style>
  :root {
    --hero-bg: #363631;
    --page-bg: #f5f5ea;
    --text-light: #ffffff;
    --brand-green: #a9c93b;
    --guide: #58d3d0;
  }
  * { margin: 0; padding: 0; box-sizing: border-box; }
  html, body {
    width: 1200px;
    height: 607px;
    overflow: hidden;
    background: var(--page-bg);
    font-family: "Arimo", Arial, sans-serif;
  }
  .page {
    position: relative;
    width: 1200px;
    height: 607px;
    background: var(--page-bg);
  }
  .hero {
    position: absolute;
    left: 0; top: 0;
    width: 1200px;
    height: 516px;
    background: var(--hero-bg);
  }
  .layout-grid {
    position: absolute;
    left: 0; top: 0;
    width: 1200px;
    height: 607px;
    pointer-events: none;
  }
  .layout-grid line { stroke: var(--guide); stroke-width: 1; }
  .brand {
    position: absolute;
    left: 216px;
    top: 46px;
    display: flex;
    align-items: center;
    gap: 10px;
    color: var(--text-light);
    font-weight: 600;
    font-size: 34px;
    letter-spacing: -0.5px;
    text-decoration: none;
  }
  .brand-dot {
    width: 30px;
    height: 30px;
    border-radius: 50%;
    background: var(--brand-green);
  }
  .main-nav {
    position: absolute;
    top: 73px;
    left: 0;
    width: 1200px;
    height: 20px;
  }
  .main-nav a {
    position: absolute;
    top: 0;
    color: var(--text-light);
    font-size: 14.5px;
    font-weight: 500;
    text-decoration: none;
    white-space: nowrap;
  }
  .hero-title {
    position: absolute;
    left: 198px;
    top: 220px;
    color: var(--text-light);
    font-size: 39px;
    font-weight: 600;
    line-height: 49px;
    letter-spacing: -0.2px;
  }
</style>
</head>
<body>
  <div class="page">
    <header class="hero">
      <a class="brand" href="#">
        <span class="brand-dot" aria-hidden="true"></span>
        <span class="brand-name">Toucan Studio</span>
      </a>
      <nav class="main-nav">
        <a href="#" style="left:515px">Home</a>
        <a href="#" style="left:591px">What we do</a>
        <a href="#" style="left:711px">Specialties</a>
        <a href="#" style="left:823px">Our process</a>
        <a href="#" style="left:946px">Contact</a>
      </nav>
      <h1 class="hero-title">Take your<br>cost control<br>to the next level</h1>
    </header>

    <svg class="layout-grid" viewBox="0 0 1400 708" width="1200" height="607" aria-hidden="true">
      <g>
        <line x1="0" y1="102" x2="1400" y2="102"/>
        <line x1="0" y1="202" x2="1400" y2="202"/>
        <line x1="0" y1="302" x2="1400" y2="302"/>
        <line x1="0" y1="402" x2="1400" y2="402"/>
        <line x1="0" y1="502" x2="1400" y2="502"/>
        <line x1="0" y1="602" x2="1400" y2="602"/>
      </g>
      <g>
        <line x1="220" y1="0" x2="220" y2="708"/><line x1="230" y1="0" x2="230" y2="708"/>
        <line x1="290" y1="0" x2="290" y2="708"/><line x1="300" y1="0" x2="300" y2="708"/><line x1="310" y1="0" x2="310" y2="708"/>
        <line x1="370" y1="0" x2="370" y2="708"/><line x1="380" y1="0" x2="380" y2="708"/><line x1="390" y1="0" x2="390" y2="708"/>
        <line x1="450" y1="0" x2="450" y2="708"/><line x1="460" y1="0" x2="460" y2="708"/><line x1="470" y1="0" x2="470" y2="708"/>
        <line x1="530" y1="0" x2="530" y2="708"/><line x1="540" y1="0" x2="540" y2="708"/><line x1="550" y1="0" x2="550" y2="708"/>
        <line x1="610" y1="0" x2="610" y2="708"/><line x1="620" y1="0" x2="620" y2="708"/><line x1="630" y1="0" x2="630" y2="708"/>
        <line x1="690" y1="0" x2="690" y2="708"/><line x1="700" y1="0" x2="700" y2="708"/><line x1="710" y1="0" x2="710" y2="708"/>
        <line x1="770" y1="0" x2="770" y2="708"/><line x1="780" y1="0" x2="780" y2="708"/><line x1="790" y1="0" x2="790" y2="708"/>
        <line x1="850" y1="0" x2="850" y2="708"/><line x1="860" y1="0" x2="860" y2="708"/><line x1="870" y1="0" x2="870" y2="708"/>
        <line x1="930" y1="0" x2="930" y2="708"/><line x1="940" y1="0" x2="940" y2="708"/><line x1="950" y1="0" x2="950" y2="708"/>
        <line x1="1010" y1="0" x2="1010" y2="708"/><line x1="1020" y1="0" x2="1020" y2="708"/><line x1="1030" y1="0" x2="1030" y2="708"/>
        <line x1="1090" y1="0" x2="1090" y2="708"/><line x1="1100" y1="0" x2="1100" y2="708"/><line x1="1110" y1="0" x2="1110" y2="708"/>
        <line x1="1170" y1="0" x2="1170" y2="708"/><line x1="1180" y1="0" x2="1180" y2="708"/>
      </g>
    </svg>
  </div>
</body>
</html>
```